Physiotherapy Clinic Post Card / Flyer

We would like a double sided postcard sized promotional card to distribute to gyms and sporting clubs, promoting our physiotherapy clinic.
The main colours of our branding are navy blue & white (As seen in sample files).
One side should be simple; with our logo. The name - "Stride & Heel Recovery Collective" and the tagline - "“The nation's trusted lower-limb recovery team.”
Also these dot points:
• Fast Rehab for lower limb injury & surgery
• Mobilisation of the foot & ankle
• Hands on therapy
• National sporting team expertise
• Podiatry (Toe-nail, skin, diabetic foot care & orthotics)
• Video pressure treadmill gait analysis and correction
• Running assessment
• Nordic walking training and sessions
And our website: www.SHRC-example.com.au & a facebook icon next to www.Facebook.com/SHRC
Also see the sample image of the runner and blue colouring. I would like this included somewhere on the postcard. I'd like to see some different design options implementing the image in different ways (front or back).
On the other side of the card I want the following text:
"SHRC is Victoria’s leading specialist provider of rehabilitation for Foot & Ankle injury and surgery.
We see our patients through their rehabilitation with an unmatched level of care & expertise.
Whether you’re an elite athlete, a weekend walker or strolling to the office, we provide the highest quality treatment & support to quickly get you back to your usual functional capacity, moving pain free with confidence.
Make an appointment at one of our FOUR Victorian locations today!"
Richmond
Level 2, 318 Wattle Grove, Richmond
1300 417 296
Brighton
Suite 7, 139 Marlin Road, Brighton 3186
9431 2785
Geelong
471 Corella Pde, Geelong 3220
5238 4169
Frankston
Suite 3, 846 Pelham Avenue, Frankston 3199
9783 5246
The images I included of my draft design are just to provide you an idea or some inspiration. Please feel free to use your creativity!

```html
<!DOCTYPE html>
<html lang="en">
<head>
<meta charset="utf-8">
<title>SHRC Clinic Flyer</title>
<link rel="stylesheet" href="https://fonts.googleapis.com/css2?family=Open+Sans:wght@400;600;700&display=swap">
<style>
  :root {
    --navy: #1c4775;
    --navy-deep: #183c63;
    --sky: #4896d2;
    --row: #2a68a4;
    --row-label: #3f8bcb;
    --ink: #1f6fa9;
    --white: #ffffff;
  }
  * { margin: 0; padding: 0; box-sizing: border-box; }
  html, body { width: 923px; height: 1200px; overflow: hidden; background: var(--white); }
  body { font-family: "Open Sans", Arial, sans-serif; }
  .flyer { position: relative; width: 923px; height: 1200px; overflow: hidden; background: var(--white); }

  .top-band { position: absolute; left: 314px; top: 0; width: 609px; height: 102px; background: var(--navy); }
  .accent-band { position: absolute; left: 314px; top: 102px; width: 609px; height: 53px; background: var(--sky); }
  .side-panel {
    position: absolute; left: 0; top: 41px; width: 332px; height: 767px;
    background: var(--sky); border-bottom-right-radius: 26px;
  }
  .photo {
    position: absolute; left: 0; width: 314px; height: 168px;
    border: 3px solid var(--white); border-left: none;
  }
  .photo--band { top: 0; background: linear-gradient(135deg, #4a4f58, #c9b8a8); }
  .photo--hands { top: 194px; background: linear-gradient(135deg, #3a4452, #d2b49c); }
  .photo--brace { top: 386px; background: linear-gradient(135deg, #2b2f36, #c8c2bc); }
  .photo--tape { top: 578px; background: linear-gradient(135deg, #d9d4cf, #b88f78); }

  .content { position: absolute; left: 332px; top: 155px; width: 591px; height: 715px; background: var(--white); }

  .logo-card {
    position: absolute; left: 428px; top: 32px; width: 404px; height: 274px;
    background: var(--white); box-shadow: 0 2px 5px rgba(0,0,0,.25);
    border-top: 6px solid var(--sky); border-bottom: 8px solid var(--navy);
  }
  .logo-name {
    position: absolute; left: 0; right: 0; top: 12px; text-align: center;
    font-size: 22px; font-weight: 400; color: var(--navy);
  }
  .logo-art {
    position: absolute; left: 40px; top: 52px; width: 324px; height: 204px;
    background: radial-gradient(ellipse at center, #2f7fa6 0%, #5aa3c2 45%, #f4f6f8 80%);
  }

  .pitch { position: absolute; left: 332px; width: 591px; text-align: center; color: var(--ink); white-space: nowrap; }
  .pitch--headline { top: 326px; font-size: 28.5px; line-height: 40.5px; }
  .pitch--headline strong { font-weight: 700; }
  .pitch--care { top: 492px; font-size: 24.5px; line-height: 34.5px; }
  .pitch--audience { top: 636px; font-size: 24.3px; line-height: 34px; }

  .divider { position: absolute; left: 0; top: 858px; width: 923px; height: 22px;
    background: linear-gradient(#ffffff, #d8dadc); }

  .locations { position: absolute; left: 0; top: 880px; width: 923px; height: 320px; background: var(--navy-deep); }
  .call-to-action {
    position: absolute; left: 0; right: 0; top: 18px; text-align: center;
    color: var(--white); font-size: 26.5px; white-space: nowrap;
  }
  .location {
    position: absolute; left: 0; width: 923px; height: 42px; background: var(--row);
    display: flex; align-items: center; color: var(--white); font-size: 23px; white-space: nowrap;
  }
  .location__town {
    width: 166px; height: 100%; background: var(--row-label);
    display: flex; align-items: center; padding-left: 26px; font-weight: 600; font-size: 26.5px;
  }
  .location__address { flex: 1; padding-left: 13px; }
  .location__phone { padding-right: 26px; }
  .location--richmond { top: 81px; }
  .location--brighton { top: 136px; }
  .location--geelong { top: 191px; }
  .location--frankston { top: 246px; }
</style>
</head>
<body>
<main class="flyer">
  <div class="top-band"></div>
  <div class="accent-band"></div>
  <div class="content"></div>

  <aside class="side-panel">
    <div class="photo photo--band" role="img" aria-label="Patient stretching a foot with a resistance band"></div>
    <div class="photo photo--hands" role="img" aria-label="Therapist mobilising a patient's foot"></div>
    <div class="photo photo--brace" role="img" aria-label="Bandaged foot in an ankle brace"></div>
    <div class="photo photo--tape" role="img" aria-label="Therapist taping an ankle"></div>
  </aside>

  <section class="logo-card">
    <div class="logo-name">Stride &amp; Heel Recovery Collective</div>
    <div class="logo-art" role="img" aria-label="Worn blue canvas sneakers"></div>
  </section>

  <p class="pitch pitch--headline"><strong>SHRC</strong> is Victoria’s leading specialist<br>provider of Rehabilitation for<br>Foot &amp; Ankle injury and surgery</p>
  <p class="pitch pitch--care">We see our patients<br>through their rehabilitation with<br>an unmatched level of care &amp; expertise.</p>
  <p class="pitch pitch--audience">Whether you’re an elite athlete,<br>a weekend walker or strolling to the office,<br>we provide the highest quality treatment<br>&amp; support to quickly get you back to<br>your usual functional capacity,<br>moving pain free with confidence.</p>

  <div class="divider"></div>

  <section class="locations">
    <p class="call-to-action">Make an appointment at one of our FOUR Victorian locations today!"</p>
    <div class="location location--richmond">
      <span class="location__town">Richmond</span>
      <span class="location__address">Level 2, 318 Wattle Grove, Richmond 312</span>
      <span class="location__phone">|&nbsp;&nbsp;Call: 1300 417 296</span>
    </div>
    <div class="location location--brighton">
      <span class="location__town">Brighton</span>
      <span class="location__address">Suite 7, 139 Marlin Road, Brighton 3186</span>
      <span class="location__phone">|&nbsp;&nbsp;Call: 9431 2785</span>
    </div>
    <div class="location location--geelong">
      <span class="location__town">Geelong</span>
      <span class="location__address">471 Corella Pde, Geelong 3220</span>
      <span class="location__phone">|&nbsp;&nbsp;Call: 5238 4169</span>
    </div>
    <div class="location location--frankston">
      <span class="location__town">Frankston</span>
      <span class="location__address">Suite 3, 846 Pelham Avenue, Frankston 3199</span>
      <span class="location__phone">|&nbsp;&nbsp;Call: 9783 5246</span>
    </div>
  </section>
</main>
</body>
</html>
```